Eye Catching Business Card for Optometrist

We've recently refreshed our logo and now we need a fresh and bold look for our business cards. We provide progressive ways to improve people's vision and protect their eye health.

Use our new logo as guidance into the colors to use. As far as style goes, I love how bold and eye catching the card is for Lanternfly Studio. Feel free to use your creative judgement.

Tagline: "Brighter days start with your eyes."

pertinent info to include:

Dr. Martin Sowerby
Optometrist

2857 Bramwell Ridge Blvd #217
Hollis Grove, MO 63390
(555) 382-7190

marty@brightlenshomeoptics.example
www.brightlenshomeoptics.example

```html
<!DOCTYPE html>
<html lang="en">
<head>
<meta charset="utf-8">
<title>Brightlens Home Optics – Business Card</title>
<link rel="stylesheet" href="https://fonts.googleapis.com/css2?family=Didact+Gothic&family=Montserrat:wght@700&family=Overlock:wght@700&display=swap">
<style>
  :root {
    --backdrop: #1c1c1c;
    --card-white: #ffffff;
    --card-black: #0c0c0c;
    --brand-red: #c1232f;
    --brand-brown: #6b5a4e;
    --brand-beige: #cbb89c;
    --ink: #1a1a1a;
    --ink-soft: #3a3a3a;
  }
  * { box-sizing: border-box; margin: 0; padding: 0; }
  html, body { width: 1200px; height: 871px; overflow: hidden; }
  body {
    background: radial-gradient(circle at 50% 40%, #2a2a2a 0%, var(--backdrop) 70%);
    font-family: "Didact Gothic", "Century Gothic", sans-serif;
    position: relative;
  }
  .card {
    position: absolute;
    left: 290px;
    width: 620px;
    height: 354px;
    border-radius: 4px;
    overflow: hidden;
    box-shadow: 0 16px 40px rgba(0,0,0,.55);
  }
  /* Back side */
  .card-back { top: 52px; background: var(--card-black); }
  .tagline {
    position: absolute;
    left: 54px; top: 104px;
    font-family: "Overlock", "Trebuchet MS", sans-serif;
    font-weight: 700;
    font-size: 40px;
    line-height: 58px;
    letter-spacing: 4px;
    color: var(--brand-beige);
  }
  .tagline .accent { color: var(--brand-red); }
  .back-brand {
    position: absolute;
    right: 44px; bottom: 54px;
    display: flex; align-items: center; gap: 10px;
  }
  .brand-square {
    width: 22px; height: 22px;
    background: var(--brand-red);
    flex: none;
  }
  .back-brand .brand-name {
    font-size: 15px;
    letter-spacing: 1px;
    color: var(--brand-beige);
  }
  /* Front side */
  .card-front { top: 446px; background: var(--card-white); }
  .front-brand {
    position: absolute;
    left: 40px; top: 70px;
    width: 250px;
    display: flex; align-items: flex-start; gap: 12px;
  }
  .front-brand .brand-square { width: 30px; height: 30px; margin-top: 4px; }
  .front-brand .brand-name {
    font-family: "Montserrat", sans-serif;
    font-weight: 700;
    font-size: 28px;
    line-height: 34px;
    color: var(--brand-red);
  }
  .contact {
    position: absolute;
    left: 340px; top: 46px;
    color: var(--ink);
  }
  .doctor-name {
    font-family: "Montserrat", sans-serif;
    font-weight: 700;
    font-size: 15px;
    letter-spacing: 1px;
  }
  .doctor-title {
    color: var(--brand-red);
    font-size: 16px;
    letter-spacing: 1px;
    margin-top: 4px;
  }
  .address {
    margin-top: 26px;
    font-size: 12px;
    line-height: 17px;
    letter-spacing: 1px;
    color: var(--ink-soft);
  }
  .contact-list { list-style: none; margin-top: 22px; }
  .contact-list li {
    display: flex; align-items: center; gap: 14px;
    font-size: 12px; letter-spacing: 1px;
    color: var(--ink-soft);
    height: 24px;
  }
  .contact-list svg { width: 14px; height: 14px; flex: none; }
  .band-brown {
    position: absolute; left: 0; bottom: 0;
    width: 150px; height: 22px;
    background: var(--brand-brown);
  }
  .block-red {
    position: absolute; left: 150px; bottom: 0;
    width: 240px; height: 92px;
    background: var(--brand-red);
  }
  .band-beige {
    position: absolute; right: 0; bottom: 0;
    width: 230px; height: 8px;
    background: var(--brand-beige);
  }
</style>
</head>
<body>
  <section class="card card-back" aria-label="Card back">
    <p class="tagline">Brighter days start<br>with your <span class="accent">eyes</span></p>
    <div class="back-brand">
      <span class="brand-square"></span>
      <span class="brand-name">Brightlens Home Optics</span>
    </div>
  </section>

  <section class="card card-front" aria-label="Card front">
    <div class="front-brand">
      <span class="brand-square"></span>
      <span class="brand-name">Brightlens Home Optics</span>
    </div>

    <div class="contact">
      <p class="doctor-name">Dr. Martin Sowerby</p>
      <p class="doctor-title">Optometrist</p>
      <p class="address">2857 Bramwell Ridge Blvd #217<br>Hollis Grove, MO 63390</p>
      <ul class="contact-list">
        <li>
          <svg viewBox="0 0 16 16" aria-hidden="true"><path d="M2 6c0-2 3-3 6-3s6 1 6 3l-2 1-1-2H5L4 7 2 6zM4 8h8l1 5H3z" fill="none" stroke="#3a3a3a" stroke-width="1.2"/></svg>
          (555) 382-7190
        </li>
        <li>
          <svg viewBox="0 0 16 16" aria-hidden="true"><rect x="1.5" y="3.5" width="13" height="9" fill="none" stroke="#3a3a3a" stroke-width="1.2"/><path d="M1.5 3.5 8 9l6.5-5.5" fill="none" stroke="#3a3a3a" stroke-width="1.2"/></svg>
          marty@brightlenshomeoptics.example
        </li>
        <li>
          <svg viewBox="0 0 16 16" aria-hidden="true"><circle cx="8" cy="8" r="6.3" fill="none" stroke="#3a3a3a" stroke-width="1.2"/><ellipse cx="8" cy="8" rx="2.6" ry="6.3" fill="none" stroke="#3a3a3a" stroke-width="1"/><path d="M1.7 8h12.6" stroke="#3a3a3a" stroke-width="1"/></svg>
          www.brightlenshomeoptics.example
        </li>
      </ul>
    </div>

    <span class="band-brown"></span>
    <span class="block-red"></span>
    <span class="band-beige"></span>
  </section>
</body>
</html>
```